A new healing and spiritual podcast needs a design.

We need a design for the podcast that will also be used on the supporting website. The name is The Quiet Lantern. The podcast will be about tapping into our own guidance to have a great life. There will be interviews, meditations, discussions on all aspects of energy healing and alternative healing techniques. The website will be where classes will be offered. Looking for something that conveys a peaceful feeling without looking too "healy-feely". Yet also want it to get peoples attention.

Target Market(s)

Metaphysical, spiritual (not religious), energy healers

Font styles to use
Serif

Requirements
Must have
• The name "The Quiet Lantern"
Nice to have
• I'd like it to be inviting, catch peoples eye, convey a peaceful feeling, yet not be boring.
Should not have
• Animated (like comic strip) images.

```html
<!DOCTYPE html>
<html lang="en">
<head>
<meta charset="utf-8">
<title>The Quiet Lantern Podcast Cover</title>
<link rel="stylesheet" href="https://fonts.googleapis.com/css2?family=Playfair+Display:wght@600&family=Poppins:wght@400&display=swap">
<style>
  :root {
    --backdrop: #dedede;
    --band: #322b2b;
    --gold: #f6c247;
    --white: #ffffff;
    --sky-top: #f7d43a;
    --sky-glow: #fbe7a0;
    --peaks: #e98c2a;
    --peak-deep: #b8471a;
    --rock: #4a0f0c;
  }
  * { margin: 0; padding: 0; box-sizing: border-box; }
  html, body {
    width: 946px;
    height: 1200px;
    overflow: hidden;
    background: var(--backdrop);
  }
  .canvas {
    position: relative;
    width: 946px;
    height: 1200px;
  }
  .cover {
    position: absolute;
    left: 73px;
    top: 200px;
    width: 800px;
    height: 800px;
    overflow: hidden;
    box-shadow: 0 4px 10px rgba(0,0,0,0.25);
    background: var(--band);
  }
  .cover__scene {
    position: absolute;
    inset: 0 0 138px 0;
    background:
      radial-gradient(ellipse 45% 30% at 50% 12%, var(--sky-glow) 0%, rgba(251,231,160,0) 100%),
      radial-gradient(ellipse 55% 55% at 50% 100%, var(--rock) 0%, var(--rock) 45%, rgba(74,15,12,0) 100%),
      linear-gradient(180deg, var(--sky-top) 0%, #f6cf62 22%, var(--peaks) 45%, var(--peak-deep) 70%, #6d1a10 100%);
  }
  .cover__band {
    position: absolute;
    left: 0;
    right: 0;
    bottom: 0;
    height: 138px;
    background: var(--band);
  }
  .title-block {
    position: absolute;
    left: 0;
    right: 0;
    top: 478px;
    display: flex;
    flex-direction: column;
    align-items: center;
  }
  .title {
    font-family: "Playfair Display", serif;
    font-weight: 600;
    font-size: 96px;
    line-height: 96px;
    color: var(--white);
    text-align: center;
    white-space: nowrap;
  }
  .subtitle {
    margin-top: 30px;
    font-family: "Poppins", sans-serif;
    font-size: 22px;
    line-height: 1;
    letter-spacing: 2px;
    color: var(--gold);
  }
</style>
</head>
<body>
  <main class="canvas">
    <section class="cover">
      <div class="cover__scene" role="img" aria-label="Photograph of a person meditating on a rocky summit above golden sunlit mountains"></div>
      <div class="cover__band"></div>
      <div class="title-block">
        <h1 class="title">The Quiet<br>Lantern</h1>
        <p class="subtitle">Podcast</p>
      </div>
    </section>
  </main>
</body>
</html>
```